New website for Pollard Law Firm at www.keepwinning-example.com

We are a professional law firm located in the Nashville, Tennessee USA area. We focus on personal injury law. We are looking for a slick new website that is user friendly for updating with new blogs, videos, etc. The primary colors should be red, black, and white. It should load extremely fast and have a good mobile component. The pages for the design will include a home page, about us, news, contact us, and practice page. The practice page will be copied for all the practice areas including motor vehicle accidents, slip and fall accidents, dog bites, etc. We have included an image which we would like to include in the new site which shows the color scheme The image is called banner-Car Wreck. The new website should NOT have gavels, court houses, law books, scales or the typical images for a law firm.

Target Market(s)

People in Tennessee involved in accidents

Industry/Entity Type

Legal services, law firm

Coding

Coded - Design and coding required

Number of Pages Required

5+ page

Font styles to use
Serif

Colors
EB3D1F
EC4F4E
F09395
F8D3D4
FCEDEE

Requirements
Should not have
• Gavels, columns, scales, law related images

```html
<!DOCTYPE html>
<html lang="en">
<head>
<meta charset="utf-8">
<title>Pollard Law Firm PLLC — Personal Injury Attorneys</title>
<link href="https://fonts.googleapis.com/css2?family=Cinzel:wght@400;600&family=Roboto:wght@400;500;700&display=swap" rel="stylesheet">
<style>
:root{
  --red:#c3252b;
  --red-deep:#a51b20;
  --red-band:#bf272c;
  --ink:#1d1d1d;
  --text:#333;
  --muted:#777;
  --line:#e4e4e4;
  --footer:#232323;
  --white:#fff;
}
*{margin:0;padding:0;box-sizing:border-box}
html,body{width:1200px;height:4123px;overflow:hidden}
body{position:relative;font-family:'Roboto',sans-serif;color:var(--text);background:var(--white)}
.abs{position:absolute}
.serif{font-family:'Cinzel',serif;font-weight:400}
a{color:inherit;text-decoration:none}

/* top bar */
.topbar{left:0;top:0;width:1200px;height:40px;border-bottom:1px solid var(--line);font-size:14px;color:#444}
.topbar span{position:absolute;top:11px;display:flex;align-items:center;gap:8px}
.topbar svg{fill:var(--red)}
.social{display:flex;gap:9px;margin-left:4px}
.social i{display:block;width:9px;height:9px;background:var(--red);border-radius:50%}

/* header */
.header{left:0;top:40px;width:1200px;height:98px}
.brand{position:absolute;display:flex;align-items:center;gap:9px;font-family:'Roboto',sans-serif;font-weight:500;white-space:nowrap}
.brand i{display:block;background:currentColor}
.brand-head{left:109px;top:36px;font-size:20px;color:var(--red)}
.brand-head i{width:12px;height:12px}
.nav{position:absolute;top:42px;font-size:14px;color:#333}
.nav.active{color:var(--red)}
.nav.active::after{content:"";position:absolute;left:0;right:0;top:26px;height:2px;background:var(--red)}
.lang{position:absolute;left:886px;top:38px;width:67px;height:27px;border:1px solid var(--red);display:flex;align-items:center;justify-content:center;gap:7px;font-size:13px;font-weight:700;color:var(--red)}
.lang i{width:14px;height:14px;border-radius:50%;background:#c5cbe0}
.login{position:absolute;left:981px;top:29px;width:106px;height:45px;border-radius:6px;background:var(--red);color:#fff;font-size:13px;font-weight:700;display:flex;align-items:center;justify-content:center;gap:8px}

/* hero */
.hero{left:0;top:138px;width:1200px;height:596px;background:#000;overflow:hidden}
.hero-photo{position:absolute;left:470px;top:0;width:730px;height:596px;background:radial-gradient(ellipse at 62% 48%,#d3262d 0%,#8f1216 38%,#2c0606 66%,#000 85%)}
.hero-kicker{left:110px;top:154px;font-size:16px;font-weight:500;color:#d8282e}
.hero-title{left:110px;top:190px;font-size:44px;line-height:47px;color:#fff;letter-spacing:1px}
.hero-text{left:111px;top:310px;width:500px;font-size:15.5px;line-height:26px;font-weight:500;color:#fff}
.btn{display:flex;align-items:center;justify-content:center;gap:10px;background:var(--red);color:#fff;font-size:13.5px;font-weight:700;border-radius:6px}
.btn svg{fill:#fff}
.hero-btn{left:112px;top:387px;width:149px;height:53px}
.dots{left:572px;top:504px;display:flex;gap:3px}
.dots i{width:8px;height:8px;border-radius:50%;background:#fff}
.dots i.on{background:none;border:1px solid #fff}

/* about */
.photo{position:absolute;border:4px solid #fff;box-shadow:0 0 8px rgba(0,0,0,.22)}
.kicker{font-family:'Cinzel',serif;font-weight:400;font-size:17px;color:#222;letter-spacing:.5px}
.h2{font-family:'Cinzel',serif;font-weight:400;font-size:35px;color:#1a1a1a;letter-spacing:1px}
.rule{width:40px;height:3px;background:var(--red)}
.about-text{left:675px;width:410px;font-size:13.5px;line-height:21.5px;color:#666}

/* practice */
.practice{left:0;top:1363px;width:1200px;height:517px;background:var(--red-band);color:#fff}
.practice .kicker,.practice .h2{color:#fff}
.practice .rule{background:#fff}
.pa-col{position:absolute;top:242px;width:215px}
.pa-col svg{stroke:#fff;fill:none;stroke-width:3}
.pa-col h3{margin-top:18px;font-size:13.5px;font-weight:700;letter-spacing:.2px}
.pa-col .pa-rule{width:34px;height:2px;background:#fff;margin-top:9px}
.pa-col p{margin-top:19px;font-size:13.5px;line-height:21.5px}
.pa-col a{display:block;margin-top:14px;font-size:11px;font-weight:700;text-decoration:underline}
.pa-div{position:absolute;top:242px;width:1px;height:206px;background:rgba(255,255,255,.55)}

/* videos */
.center{left:0;width:1200px;text-align:center}
.center .rule{margin:0 auto}
.kicker.red{color:var(--red)}
.thumb{position:absolute;top:2110px;width:317px;height:226px}
.play{position:absolute;left:50%;top:50%;width:48px;height:48px;margin:-24px 0 0 -24px;border-radius:50%;background:var(--red);display:flex;align-items:center;justify-content:center}

/* news */
.news-left{left:110px;top:2645px;width:425px}
.news-date{display:flex;align-items:center;gap:20px;font-size:13.5px;font-weight:700;color:#222}
.news-left h3{margin-top:28px;font-size:13.5px;font-weight:700;color:#222}
.news-left p{margin-top:16px;font-size:13.5px;line-height:30px;color:#666}
.news-list{left:619px;top:2640px;width:470px;box-shadow:0 0 10px rgba(0,0,0,.12);background:#fff}
.news-item{padding:19px 32px 17px;border-top:1px solid var(--line);height:114px}
.news-item h4{font-size:13px;font-weight:700;color:#222}
.news-item p{margin-top:12px;font-size:13px;line-height:24px;color:#777}
.news-item.current{background:var(--red);border:0;height:118px;position:relative}
.news-item.current h4,.news-item.current p{color:#fff}
.news-item.current::before{content:"";position:absolute;left:-10px;top:52px;border:10px solid transparent;border-left:0;border-right-color:var(--red)}

/* appointment */
.booking{left:0;top:3202px;width:1200px;height:550px;background:var(--red-deep);color:#fff}
.booking .kicker,.booking .h2{color:#fff}
.booking .rule{background:#fff}
.field{position:absolute;background:#fff;border:1px solid #ddd;font-size:13px;color:#888;padding:16px 12px}
.submit{position:absolute;left:510px;top:419px;width:180px;height:53px;border-radius:27px;background:#2a2a2a;color:#fff;font-size:13.5px;font-weight:700;display:flex;align-items:center;justify-content:center;gap:10px}
.submit svg{fill:#fff}

/* footer */
.footer{left:0;top:3752px;width:1200px;height:323px;background:var(--footer);color:#fff}
.fcol{position:absolute;top:66px}
.fcol h5{font-size:13.5px;font-weight:700;text-decoration:underline;margin-bottom:20px}
.fcol li{list-style:none;font-size:14px;height:38.5px;display:flex;gap:22px;align-items:flex-start}
.fcol li svg{fill:var(--red);flex:none;margin-top:3px}
.fcol li .chev{color:var(--red);font-size:12px;width:8px}
.brand-foot{left:836px;top:140px;font-size:26px;color:#fff}
.brand-foot i{width:14px;height:14px}
.copy{left:0;top:4075px;width:1200px;height:48px;background:var(--red);color:#fff;font-size:13.5px;text-align:center;line-height:48px}
</style>
</head>
<body>

<!-- Top bar -->
<div class="abs topbar">
  <span style="left:110px"><svg width="13" height="10" viewBox="0 0 13 10"><path d="M0 0h13v10H0zM1 1l5.5 4.5L12 1z" fill-rule="evenodd"/></svg>info@pollard-example.com</span>
  <span style="left:338px"><svg width="12" height="12" viewBox="0 0 12 12"><rect x="0" y="3" width="12" height="9" rx="1"/><rect x="3" y="0" width="6" height="4"/></svg>(615) 555-0141</span>
  <span style="left:502px"><svg width="11" height="11" viewBox="0 0 11 11"><path d="M2 0l2 3-1.2 1.2a6 6 0 0 0 4 4L8 7l3 2-1 2C4.5 11 0 6.5 0 1z"/></svg>(615) 555-0140</span>
  <span style="left:891px">Follow us <span class="social" style="position:static"><i></i><i></i><i></i></span></span>
  <span style="left:1064px"><svg width="13" height="13" viewBox="0 0 13 13"><circle cx="5.5" cy="5.5" r="4" fill="none" stroke="#c3252b" stroke-width="2"/><path d="M8.5 8.5l3.5 3.5" stroke="#c3252b" stroke-width="2.2"/></svg></span>
</div>

<!-- Header -->
<header class="abs header">
  <div class="brand brand-head"><i></i>Pollard Law Firm</div>
  <a class="nav active" style="left:437px">Home</a>
  <a class="nav" style="left:498px">About us</a>
  <a class="nav" style="left:578px">Practicr Area</a>
  <a class="nav" style="left:683px">Latest News</a>
  <a class="nav" style="left:786px">Contact Us</a>
  <div class="lang"><i></i>ENG</div>
  <a class="login">LOG IN <svg width="10" height="12" viewBox="0 0 10 12" fill="#fff"><path d="M2 5V3.5a3 3 0 0 1 6 0V5h1v7H1V5zm1.5 0h3V3.5a1.5 1.5 0 0 0-3 0z"/></svg></a>
</header>

<!-- Hero -->
<section class="abs hero">
  <div class="hero-photo" role="img" aria-label="Close-up of a red car after a wreck, with shattered glass flying from the headlight and windshield"></div>
  <div class="abs hero-kicker">POLLARD LAW FIRM PLLC</div>
  <h1 class="abs hero-title serif">DON’T LOSE WHAT’S<br>LEGALLY YOURS</h1>
  <p class="abs hero-text">We fight against billion dollar insurance companies, billion dollar corporations, and the State of Tennessee..and we win!</p>
  <a class="abs btn hero-btn">GET STARTED <svg width="13" height="13" viewBox="0 0 13 13"><circle cx="6.5" cy="6.5" r="6.5"/><path d="M5 3.5l3 3-3 3" stroke="#c3252b" stroke-width="1.8" fill="none"/></svg></a>
  <div class="abs dots"><i></i><i></i><i class="on"></i><i></i><i></i></div>
</section>

<!-- About -->
<section>
  <div class="photo" style="left:112px;top:829px;width:232px;height:211px;background:linear-gradient(135deg,#8a8a8a,#c9302e 55%,#e8e8e8)" role="img" aria-label="Paramedic helping an injured woman at an accident scene"></div>
  <div class="photo" style="left:362px;top:896px;width:147px;height:136px;background:linear-gradient(180deg,#3e4a5c,#6d7889 60%,#b8392f)" role="img" aria-label="Warning triangle on a wet road with traffic behind"></div>
  <div class="photo" style="left:192px;top:1059px;width:149px;height:136px;background:linear-gradient(135deg,#d8c7b6,#b98b6a 50%,#e6d8e4)" role="img" aria-label="Mother comforting her young daughter at home"></div>
  <div class="photo" style="left:362px;top:1053px;width:228px;height:208px;background:linear-gradient(135deg,#dfe4ea,#9fa9b6 50%,#2f3a4c)" role="img" aria-label="Attorney reviewing documents with a client in an office"></div>

  <div class="abs kicker" style="left:675px;top:843px">Who We Are</div>
  <h2 class="abs h2" style="left:675px;top:878px">ABOUT US</h2>
  <div class="abs rule" style="left:677px;top:935px"></div>
  <p class="abs about-text" style="top:957px">There are many law firms in Tennessee who claim to be trial lawyers, but their attorneys have never seen a courtroom. We have tried hundreds of cases to verdict and we have helped thousands of people in the Tennessee courts. We fight against billion dollar insurance companies, billion dollar corporations, and the State of Tennessee..and we win!</p>
  <p class="abs about-text" style="top:1107px">It is very hard not to take each case personally. Our clients include victims of personal injury who did not ask for the pain from a car wreck; professionals</p>
  <a class="abs btn" style="left:675px;top:1192px;width:174px;height:50px">MORE ABOUT US <svg width="13" height="13" viewBox="0 0 13 13"><circle cx="6.5" cy="6.5" r="6.5"/><path d="M5 3.5l3 3-3 3" stroke="#c3252b" stroke-width="1.8" fill="none"/></svg></a>
</section>

<!-- Practice areas -->
<section class="abs practice">
  <div class="abs kicker" style="left:112px;top:73px">Why Us</div>
  <h2 class="abs h2" style="left:110px;top:108px">PRACTICE AREAS</h2>
  <div class="abs rule" style="left:112px;top:162px"></div>
  <div class="abs" style="left:525px;top:72px;width:1px;height:101px;background:rgba(255,255,255,.6)"></div>
  <p class="abs" style="left:581px;top:88px;width:510px;font-size:13.5px;line-height:21.5px">Lorem ipsum dolor sit amet, consectetur adipiscing elit, sed do eiusmod tempor incididunt ut labore et dolore magna aliqua. Ut enim ad minim veniam, quis nostrud exercitation ullamco laboris nisi</p>

  <div class="pa-col" style="left:134px">
    <svg width="56" height="40" viewBox="0 0 56 40"><circle cx="12" cy="28" r="9"/><circle cx="44" cy="28" r="9"/><path d="M12 28l14-14h12l6 14"/></svg>
    <h3>MOTOR VEHICLE ACCIDENTS</h3><div class="pa-rule"></div>
    <p>Lorem ipsum dolor sit amet, consectetur adipiscing elit, sed do eiusmod tempor incididunt</p>
    <a>VIEW MORE &nbsp;»</a>
  </div>
  <div class="pa-div" style="left:349px"></div>
  <div class="pa-col" style="left:376px">
    <svg width="56" height="40" viewBox="0 0 56 40"><path d="M24 4L44 38H4z"/><path d="M24 16v10M24 30v3"/></svg>
    <h3>SLIP AND FALL ACCIDENTS</h3><div class="pa-rule"></div>
    <p>Lorem ipsum dolor sit amet, consectetur adipiscing elit, sed do eiusmod tempor incididunt</p>
    <a>VIEW MORE &nbsp;»</a>
  </div>
  <div class="pa-div" style="left:592px"></div>
  <div class="pa-col" style="left:618px">
    <svg width="56" height="40" viewBox="0 0 56 40"><rect x="4" y="4" width="32" height="32" rx="4"/><path d="M12 20h16M20 12v16"/></svg>
    <h3>DOG BITES</h3><div class="pa-rule"></div>
    <p>Lorem ipsum dolor sit amet, consectetur adipiscing elit, sed do eiusmod tempor incididunt</p>
    <a>VIEW MORE &nbsp;»</a>
  </div>
  <div class="pa-div" style="left:834px"></div>
  <div class="pa-col" style="left:861px">
    <svg width="56" height="40" viewBox="0 0 56 40"><path d="M6 36V18l20-14 20 14v18z"/><path d="M20 36V24h12v12"/></svg>
    <h3>CHILD CUSTODY</h3><div class="pa-rule"></div>
    <p>Lorem ipsum dolor sit amet, consectetur adipiscing elit, sed do eiusmod tempor incididunt ut</p>
    <a>VIEW MORE &nbsp;»</a>
  </div>
</section>

<!-- Videos -->
<section>
  <div class="abs center" style="top:1972px"><div class="kicker red">Videos</div></div>
  <div class="abs center" style="top:2005px"><h2 class="h2">OUR VIDEOS</h2></div>
  <div class="abs center" style="top:2063px"><div class="rule"></div></div>
  <div class="thumb" style="left:112px;background:linear-gradient(135deg,#b9bcbf,#e7e3df 45%,#5c5f63)" role="img" aria-label="Older woman looking at her phone while driving"><div class="play"><svg width="16" height="18" viewBox="0 0 16 18" fill="#fff"><path d="M2 1l13 8-13 8z"/></svg></div></div>
  <div class="thumb" style="left:442px;background:linear-gradient(180deg,#b7bcc0,#8e9499 55%,#5d6266)" role="img" aria-label="Semi-truck driving on a highway in the rain"><div class="play"><svg width="16" height="18" viewBox="0 0 16 18" fill="#fff"><path d="M2 1l13 8-13 8z"/></svg></div></div>
  <div class="thumb" style="left:771px;background:linear-gradient(180deg,#b9d0e6,#5f8a4e 45%,#7d7f80)" role="img" aria-label="Car driving past a roadside speed sign on a tree-lined road"><div class="play"><svg width="16" height="18" viewBox="0 0 16 18" fill="#fff"><path d="M2 1l13 8-13 8z"/></svg></div></div>
  <div class="abs" style="left:0;top:2440px;width:1200px;height:1px;background:var(--line)"></div>
</section>

<!-- Latest news -->
<section>
  <div class="abs center" style="top:2503px"><div class="kicker">Resources</div></div>
  <div class="abs center" style="top:2536px"><h2 class="h2">LATEST NEWS</h2></div>
  <div class="abs center" style="top:2594px"><div class="rule"></div></div>

  <article class="abs news-left">
    <div class="news-date"><svg width="16" height="16" viewBox="0 0 16 16" fill="#c3252b"><path d="M0 3h16v13H0zM1.5 6v8.5h13V6z" fill-rule="evenodd"/><rect x="3" y="0" width="2" height="4"/><rect x="11" y="0" width="2" height="4"/><rect x="3" y="8" width="2" height="2"/><rect x="7" y="8" width="2" height="2"/><rect x="11" y="8" width="2" height="2"/><rect x="3" y="11" width="2" height="2"/><rect x="7" y="11" width="2" height="2"/></svg>JULY 1, 2019</div>
    <h3>TRUCKING COMPANY OFFERS 6 FIGURE SETTLEMENT</h3>
    <p>On a Thursday afternoon, our client was traveling to work when suddenly a semi-truck ran through a stop sign and crashed into the side of our client’s truck causing him to spin out of control. Our client believed he was okay, but later that afternoon began to</p>
    <p>feel pain in his shoulder. Eventually, he would learn that he suffered from a torn ligament and he would require surgery.</p>
    <p>At first, the insurance company claimed the wreck was minor and the client’s claim was only worth a few thousand dollars. After several months of litigation and discovery, we learned this was not the first time this driver was found in an accident.</p>
  </article>

  <div class="abs news-list">
    <div class="news-item current"><h4>TRUCKING COMPANY OFFERS 6 FIGURE SETTLEMENT</h4><p>On a Thursday afternoon, our client was traveling to work when suddenly a semi-truck ran through a stop sign</p></div>
    <div class="news-item"><h4>FAMILY SERVICES CHOOSES TO DISMISS CASE</h4><p>In a case in Harbor County, the Harbor County Family Support Office was contacted about a family</p></div>
    <div class="news-item"><h4>POLLARD OBTAINS JURY VERDICT OF 61 X MEDICAL BILLS</h4><p>In 2016, a client was traveling down a road and stopped in traffic when she was hit by another driver in the rear end.</p></div>
    <div class="news-item"><h4>INSURANCE COMPANY PAYS FOR FACIAL FRACTURES</h4><p>On a dark night in Murfreesboro, Tennessee, a young woman was riding in the car with her friends when the driver</p></div>
  </div>
</section>

<!-- Book an appointment -->
<section class="abs booking">
  <div class="abs center" style="top:73px"><div class="kicker">Let’s Chat</div></div>
  <div class="abs center" style="top:106px"><h2 class="h2">BOOK AN APPOINTMENT</h2></div>
  <div class="abs center" style="top:165px"><div class="rule"></div></div>
  <div class="field" style="left:117px;top:240px;width:235px;height:51px">First Name</div>
  <div class="field" style="left:360px;top:240px;width:237px;height:51px">Email Address</div>
  <div class="field" style="left:605px;top:240px;width:235px;height:51px">Phone No</div>
  <div class="field" style="left:848px;top:240px;width:237px;height:51px">Address</div>
  <div class="field" style="left:117px;top:302px;width:968px;height:85px;padding-top:12px">Message</div>
  <a class="submit">REGISTER NOW <svg width="13" height="13" viewBox="0 0 13 13"><circle cx="6.5" cy="6.5" r="6.5"/><path d="M5 3.5l3 3-3 3" stroke="#2a2a2a" stroke-width="1.8" fill="none"/></svg></a>
</section>

<!-- Footer -->
<footer class="abs footer">
  <div class="fcol" style="left:114px">
    <h5>FIND US ON</h5>
    <ul>
      <li style="height:76px"><svg width="10" height="14" viewBox="0 0 10 14"><path d="M5 0a5 5 0 0 1 5 5c0 4-5 9-5 9S0 9 0 5a5 5 0 0 1 5-5zm0 3a2 2 0 1 0 0 4 2 2 0 0 0 0-4z" fill-rule="evenodd"/></svg><span style="line-height:38px;margin-top:-11px">1480 Maple Ridge Drive | Suite<br>210 | Franklin, TN 37064</span></li>
      <li><svg width="11" height="11" viewBox="0 0 11 11"><path d="M2 0l2 3-1.2 1.2a6 6 0 0 0 4 4L8 7l3 2-1 2C4.5 11 0 6.5 0 1z"/></svg>(615) 555-0140</li>
      <li><svg width="13" height="10" viewBox="0 0 13 10"><path d="M0 0h13v10H0zM1 1l5.5 4.5L12 1z" fill-rule="evenodd"/></svg>office@pollardlawfirm-example.com</li>
    </ul>
  </div>
  <div class="fcol" style="left:400px">
    <h5>PRACTICE AREAS</h5>
    <ul>
      <li><span class="chev">»</span>Motor vehicle accidents</li>
      <li><span class="chev">»</span>Slip and fall accidents</li>
      <li><span class="chev">»</span>Dog bites</li>
      <li><span class="chev">»</span>Personal Injury</li>
      <li><span class="chev">»</span>Child Custody</li>
    </ul>
  </div>
  <div class="fcol" style="left:658px">
    <h5>OTHER LINKS</h5>
    <ul>
      <li><span class="chev">»</span>Home</li>
      <li><span class="chev">»</span>About Us</li>
      <li><span class="chev">»</span>Practice Areas</li>
      <li><span class="chev">»</span>Blog</li>
      <li><span class="chev">»</span>Contact Us</li>
    </ul>
  </div>
  <div class="brand brand-foot"><i></i>Pollard Law Firm</div>
</footer>
<div class="abs copy">© 2021 Pollard Law Firm, PLLC. All Rights Reserved</div>

</body>
</html>
```